Brindle's Business Card

I need some designs for a new business card including the new logo attached. An old example of our business card is also attached to show all the data that should be included on the new design.
**I added some more examples someone had mocked up**

Contact Information for Business Card

Should include all info on other examples uploaded.

```html
<!DOCTYPE html>
<html lang="en">
<head>
<meta charset="utf-8">
<title>Brindle's Business Card</title>
<link rel="stylesheet" href="https://fonts.googleapis.com/css2?family=Montserrat:wght@600&family=Poppins:wght@600&family=Roboto:wght@400&display=swap">
<style>
  :root {
    --backdrop: #2c2c2c;
    --card-white: #ffffff;
    --brand-red: #ec2027;
    --brand-red-deep: #e42329;
    --brand-blue: #0f73bd;
    --ink: #2a2a2a;
  }
  html, body {
    margin: 0;
    padding: 0;
    width: 1200px;
    height: 1200px;
    overflow: hidden;
    background: var(--backdrop);
  }
  .stage {
    position: relative;
    width: 1200px;
    height: 1200px;
  }
  .card {
    position: absolute;
    left: 239px;
    width: 722px;
    height: 412px;
    border-radius: 25px;
    overflow: hidden;
    box-shadow: 0 14px 30px rgba(0,0,0,0.45);
  }
  .card-front { top: 140px; background: var(--card-white); }
  .card-back { top: 645px; background: var(--brand-blue); }
  .card-shape {
    position: absolute;
    inset: 0;
    width: 100%;
    height: 100%;
  }
  .accent-panel {
    position: absolute;
    left: 400px;
    top: 0;
    right: 0;
    bottom: 0;
    background: linear-gradient(160deg, var(--brand-red-deep), var(--brand-red));
    border-top-left-radius: 100% 100%;
  }
  .brand {
    position: absolute;
    display: flex;
    align-items: center;
    gap: 16px;
  }
  .brand-dot {
    width: 62px;
    height: 62px;
    border-radius: 50%;
    flex: none;
  }
  .brand-name {
    font-family: 'Montserrat', sans-serif;
    font-weight: 600;
    font-size: 54px;
    line-height: 1;
    letter-spacing: 0.5px;
  }
  .card-front .brand { left: 45px; top: 70px; }
  .card-front .brand-dot { background: var(--brand-red); }
  .card-front .brand-name { color: var(--brand-blue); }
  .card-back .brand { left: 232px; top: 172px; }
  .card-back .brand-dot { background: var(--card-white); }
  .card-back .brand-name { color: var(--card-white); }
  .holder-name {
    position: absolute;
    left: 51px;
    top: 261px;
    margin: 0;
    font-family: 'Poppins', sans-serif;
    font-weight: 600;
    font-size: 40px;
    line-height: 1;
    color: var(--brand-blue);
  }
  .contact-list {
    position: absolute;
    left: 51px;
    top: 314px;
    margin: 0;
    padding: 0;
    list-style: none;
    font-family: 'Roboto', sans-serif;
    font-size: 19.5px;
    color: var(--ink);
  }
  .contact-list li {
    display: flex;
    align-items: center;
    height: 29px;
  }
  .contact-icon {
    width: 18px;
    height: 16px;
    margin-right: 15px;
    flex: none;
  }
  .promise {
    position: absolute;
    right: 48px;
    top: 312px;
    margin: 0;
    text-align: right;
    font-family: 'Roboto', sans-serif;
    font-size: 19.5px;
    line-height: 29px;
    color: var(--card-white);
  }
</style>
</head>
<body>
<main class="stage">
  <section class="card card-front" aria-label="Card front">
    <div class="accent-panel" role="img" aria-label="Red flame-style decorative area"></div>
    <div class="brand">
      <span class="brand-dot"></span>
      <span class="brand-name">BRINDLE'S</span>
    </div>
    <h1 class="holder-name">DALE BRINDLE</h1>
    <ul class="contact-list">
      <li>
        <svg class="contact-icon" viewBox="0 0 20 20" aria-hidden="true"><path fill="var(--brand-red)" d="M5 1 L8 5 L6.5 7.5 C7.5 10 9.5 12.5 12.5 13.5 L14.5 12 L18.5 15 L16.5 18.5 C9 18 2.5 11.5 2 4 Z"/></svg>
        555.014.2290
      </li>
      <li>
        <svg class="contact-icon" viewBox="0 0 20 16" aria-hidden="true"><rect x="1" y="2" width="18" height="12" fill="var(--brand-red)"/><path d="M1.5 2.5 L10 9 L18.5 2.5" fill="none" stroke="var(--card-white)" stroke-width="1.6"/></svg>
        service@brindlecomfort.com
      </li>
    </ul>
    <p class="promise">Licensed and Insured<br>Family Owned and Operated</p>
  </section>

  <section class="card card-back" aria-label="Card back">
    <svg class="card-shape" viewBox="0 0 1163 663" preserveAspectRatio="none" aria-hidden="true">
      <path fill="var(--brand-red)" d="M0 0 L40 0 C60 110 120 180 170 250 C260 370 310 470 308 663 L0 663 Z"/>
    </svg>
    <div class="brand">
      <span class="brand-dot"></span>
      <span class="brand-name">BRINDLE'S</span>
    </div>
  </section>
</main>
</body>
</html>
```